Drinks menu for our organic restaurant

We need a new menu design for our restaurant based in Glastonbury, UK. We are an organic, wholefood restaurant with an ethical sourcing policy, off...

Target Market(s)

Ladies that Lunch, foodies, people with an specific diet - health consious, vegan, organic, gluten-free.

Industry/Entity Type

Restaurant

Requirements
Must have
• The items on the menu may change from time to time so it must be in a format that we can edit. We will be re-printing the menus often on our inhouse colour printer.
Nice to have
• Our style is simple, rustic, and the restaurant is furnished in natural woods and earthy colours.
Should not have
• Nothing garish - we are a small independent restaurant and want to represent our individual and quirky style.

```html
<!DOCTYPE html>
<html lang="en">
<head>
<meta charset="utf-8">
<title>Drinks Menu</title>
<link href="https://fonts.googleapis.com/css2?family=Comfortaa:wght@400;700&family=Raleway:ital,wght@0,400;0,500;1,400&display=swap" rel="stylesheet">
<style>
:root{
  --backdrop:#b4b4b4;
  --paper:#fdf6dc;
  --olive:#9ba13a;
  --ink:#6f6a3e;
  --ink-soft:#8a8456;
  --rule:#a6a36a;
  --alert:#c2412d;
}
*{box-sizing:border-box;margin:0;padding:0}
html,body{width:1200px;height:1000px;overflow:hidden}
body{background:var(--backdrop);font-family:"Raleway",sans-serif;color:var(--ink);position:relative}
.page{position:absolute;top:149px;width:255px;height:660px;background:var(--paper)}
.page--3{left:72px}.page--4{left:327px}.page--5{left:618px}.page--6{left:873px}
.page--4,.page--6{box-shadow:inset 6px 0 8px -6px rgba(0,0,0,.12)}
.section-title{position:absolute;left:0;right:0;text-align:center;font-family:"Comfortaa",sans-serif;color:var(--olive);font-size:33px;font-weight:400;line-height:1}
.section-title--bold{font-weight:700}
.section-title--compact{font-size:28px}
.page-number{position:absolute;bottom:8px;font-size:9px;color:var(--ink)}
.page--3 .page-number,.page--5 .page-number{left:17px}
.page--4 .page-number,.page--6 .page-number{right:17px}
.intro{position:absolute;left:28px;width:185px;font-size:5px;line-height:1.35;color:var(--ink-soft)}
.intro p+p{margin-top:5px}
.blend{position:absolute;left:28px;font-size:8.5px}
.note{display:block;font-size:4.6px;font-style:italic;color:var(--ink-soft);line-height:1.25}
.coffee-table{position:absolute;left:28px;top:158px;width:199px;height:154px;border:1px solid var(--rule);display:grid;grid-template-columns:122px 26px 26px 1fr;padding-top:5px}
.coffee-table .col{border-left:1px solid var(--rule);font-size:6.2px;line-height:10.75px;padding-left:4px}
.coffee-table .col:first-child{border:none;font-size:8.5px;padding-left:6px}
.warmers-band{position:absolute;left:0;right:0;top:364px;height:7px;background:var(--olive);font-size:5px;color:var(--paper);line-height:7px}
.warmers-band span{position:absolute}
.warmer{position:absolute;left:28px;width:210px;font-size:8.5px}
.warmer .price{position:absolute;top:1px;font-size:6px;line-height:1.3}
.warmer .p1{left:148px}.warmer .p2{left:184px}
.list{position:absolute;left:16px;right:16px}
.item{display:flex;align-items:baseline;font-size:8.5px;white-space:nowrap}
.item .leader{flex:1;border-bottom:1px dotted var(--rule);margin:0 2px;transform:translateY(-2px)}
.item .cost{font-size:5.8px}
.item svg{width:10px;height:10px;margin-left:1px;align-self:center}
.entry{overflow:hidden}
.entry .note{white-space:normal}
.page--4 .list{left:41px;right:41px}
.page--4 .entry{height:24.5px}
.iced .entry{height:19px}
.page--5 .list{left:17px;right:17px}
.page--5 .entry{height:24px}
.page--6 .list{left:14px;right:19px}
.page--6 .entry{height:24px}
.page--6 .note{font-size:4.3px}
.legend{position:absolute;left:16px;right:16px;top:585px;height:24px;border-top:1px solid var(--rule);border-bottom:1px solid var(--rule);display:flex;justify-content:center;align-items:center;gap:28px;font-size:5px;text-transform:uppercase;color:var(--ink)}
.legend span{display:flex;align-items:center;gap:4px}
.legend svg{width:10px;height:10px}
.defs{position:absolute;width:0;height:0}
</style>
</head>
<body>
<svg class="defs" aria-hidden="true">
  <defs>
    <symbol id="leaf" viewBox="0 0 20 20"><path d="M4 17C4 9 9 4 17 3c0 8-5 13-12 13z" fill="#9ba13a"/><path d="M3 18c3-5 6-8 10-11" stroke="#fdf6dc" stroke-width="1.2" fill="none"/><path d="M6 12c-3-1-4-4-3-7 3 1 4 3 3 7z" fill="#9ba13a"/></symbol>
    <symbol id="nofree" viewBox="0 0 20 20"><circle cx="10" cy="10" r="8" fill="none" stroke="#c2412d" stroke-width="2"/><path d="M4.5 4.5l11 11" stroke="#c2412d" stroke-width="2"/></symbol>
    <symbol id="nut" viewBox="0 0 20 20"><circle cx="10" cy="10" r="8.5" fill="none" stroke="#9ba13a" stroke-width="1.5"/><ellipse cx="10" cy="10.5" rx="3.2" ry="5" fill="#9ba13a"/></symbol>
    <symbol id="celery" viewBox="0 0 20 20"><circle cx="10" cy="10" r="8.5" fill="none" stroke="#9ba13a" stroke-width="1.5"/><path d="M5 6l9 9M7 5l8 8" stroke="#9ba13a" stroke-width="1.5"/></symbol>
  </defs>
</svg>

<!-- Page 03: Coffee & Warmers -->
<section class="page page--3">
  <h1 class="section-title" style="top:30px">Coffee</h1>
  <div class="intro" style="top:68px">
    <p>Our coffee is organic, 100% speciality grade and sourced from small producers that can be traced right through the supply chain.</p>
    <p>This not only ensures a fantastic flavour, but a fair price for the growers.</p>
  </div>
  <div class="blend" style="top:110px">Old Oak Blend<span class="note">A light roast with caramel sweetness.</span></div>
  <div class="blend" style="top:134px">Honduras<span class="note">Single-origin beans, deep, robust and full-bodied</span></div>
  <div class="coffee-table">
    <div class="col">Short Cortado<br>Latte<br>Cappuccino<br>Americano (black)<br>White Americano<br>Macchiato<br>Espresso<br>Mocha<br>Flat White<br>Babychino<br>Extra Shot<br>Cream<br>Meadowlark Vegan Syrup</div>
    <div class="col">2.10<br>2.30<br>2.30<br>1.90<br>2.20<br>2.00<br>1.90<br>2.30<br>2.50<br>0.60p</div>
    <div class="col">2.60<br>2.80<br>2.80<br>2.40<br>2.60<br>2.40<br>2.30<br>3.00<br>3.00<br>1.00<br>+60p<br>+1.00<br>+50p</div>
    <div class="col"><br>3.60<br>3.60<br>2.90<br>3.10<br>3.00<br>2.80<br>3.80</div>
  </div>
  <h2 class="section-title" style="top:330px">Warmers</h2>
  <div class="warmers-band"><span style="left:170px">medium</span><span style="left:212px">large</span></div>
  <div class="warmer" style="top:378px">Hot Chocolate<span class="note">Add squirty cream</span><span class="price p1">2.90<br>3.60</span><span class="price p2">3.60<br>4.30</span></div>
  <div class="warmer" style="top:404px">Vegan, sugar-free hot cocoa <svg width="10" height="10"><use href="#nofree"/></svg><span class="price p1">3.00</span><span class="price p2">4.00</span></div>
  <div class="warmer" style="top:427px">Warm farmhouse apple juice<span class="price p1">2.40</span><span class="price p2">3.40</span></div>
  <div class="warmer" style="top:449px">December Apple<span class="note">apple, ginger, spice</span><span class="price p1">2.80</span><span class="price p2">3.60</span></div>
  <div class="warmer" style="top:473px">Betty<span class="note">ginger, lemon, honey, water</span><span class="price p1">2.50</span><span class="price p2">3.00</span></div>
  <div class="warmer" style="top:498px">Cuddle<span class="note">oat milk, vanilla, honey, spice</span><span class="price p1">3.00</span><span class="price p2">3.60</span></div>
  <div class="warmer" style="top:522px">Spicy Cuddle<span class="note">with spiced organic rum</span><span class="price p1">5.50</span><span class="price p2">–</span></div>
  <div class="warmer" style="top:545px">Organic Chai Latte <svg width="10" height="10"><use href="#leaf"/></svg><span class="price p1">3.00</span><span class="price p2">4.00</span></div>
  <div class="warmer" style="top:568px">Hot Toddy<span class="note">ginger, lemon, honey, whisky</span><span class="price p1">5.50</span></div>
  <div class="warmer" style="top:593px">Mulled Cider<span class="note">add a shot of rum, brandy or whisky</span><span class="price p1">3.50<br>3.00</span></div>
  <span class="page-number">03</span>
</section>

<!-- Page 04: Soft Drinks & Iced Drinks -->
<section class="page page--4">
  <h2 class="section-title section-title--compact" style="top:29px">Soft Drinks</h2>
  <div class="list" style="top:63px">
    <div class="entry"><div class="item">Blackcurrant Squash<svg><use href="#leaf"/></svg><span class="leader"></span><span class="cost">1.75</span></div><span class="note">BROOKS, organic (250ml)</span></div>
    <div class="entry"><div class="item">Cola<svg><use href="#leaf"/></svg><span class="leader"></span><span class="cost">3.00</span></div><span class="note">KINDRED COLA, organic (330ml)</span></div>
    <div class="entry"><div class="item">Sicilian Lemonade<span class="leader"></span><span class="cost">3.00</span></div><span class="note">HOLLOWAY, organic (320ml)</span></div>
    <div class="entry"><div class="item">Elderflower Presse<svg><use href="#leaf"/></svg><span class="leader"></span><span class="cost">3.00</span></div><span class="note">MARLOW, organic (275ml)</span></div>
    <div class="entry"><div class="item">Ginger Beer<svg><use href="#leaf"/></svg><span class="leader"></span><span class="cost">3.00</span></div><span class="note">HOLLOWAY, organic (320ml)</span></div>
    <div class="entry"><div class="item">'Simply Minted'<span class="leader"></span><span class="cost">2.75</span></div><span class="note">BRAMBLE HOG (250ml). Sparkling apple juice with pink grapefruit, mint and a twist of lime</span></div>
    <div class="entry"><div class="item">Kombucha<span class="leader"></span><span class="cost">3.25</span></div><span class="note">SOLSTICE (275ml). Green Tea &amp; Wild Berry.</span></div>
    <div class="entry"><div class="item">Orange Juice<span class="leader"></span><span class="cost">3.00</span></div><span class="note">Freshly-squeezed (250ml)</span></div>
    <div class="entry"><div class="item">Carrot Juice<svg><use href="#leaf"/></svg><span class="leader"></span><span class="cost">3.00</span></div><span class="note">VERDA, organic (330ml)</span></div>
    <div class="entry"><div class="item">Farmhouse Apple Juice<span class="leader"></span><span class="cost">2.60</span></div><span class="note">BRAMBLE HOG (250ml)</span></div>
    <div class="entry"><div class="item">Milkshake<span class="leader"></span><span class="cost">2.50</span></div><span class="note">DALEFORD organic (250ml), strawberry or chocolate</span></div>
    <div class="entry"><div class="item">Indian Tonic Water<span class="leader"></span><span class="cost">2.00</span></div><span class="note">FERNLEAF (200ml)</span></div>
    <div class="entry"><div class="item">Aromatic Tonic Water<span class="leader"></span><span class="cost">3.00</span></div><span class="note">FERNLEAF (200ml)</span></div>
    <div class="entry"><div class="item">Tor Spring Water<span class="leader"></span><span class="cost">2.20(33cl)/ 4.00(75cl)</span></div><span class="note">Still or sparkling</span></div>
  </div>
  <h2 class="section-title section-title--compact" style="top:446px">Iced Drinks</h2>
  <div class="list iced" style="top:492px">
    <div class="entry"><div class="item">Iced Tea (regular/ herbal)<span class="leader"></span><span class="cost">2.80/ 3.80</span></div></div>
    <div class="entry"><div class="item">Iced Coffee<span class="leader"></span><span class="cost">3.30/ 5.00</span></div></div>
    <div class="entry"><div class="item">Iced Mocha<span class="leader"></span><span class="cost">3.50/ 5.00</span></div></div>
    <div class="entry"><div class="item">Affogato<span class="leader"></span><span class="cost">4.00</span></div></div>
  </div>
  <div class="legend"><span><svg><use href="#nofree"/></svg>Sugar free</span><span><svg><use href="#leaf"/></svg>Organic</span></div>
  <span class="page-number">04</span>
</section>

<!-- Page 05: Beer and Cider -->
<section class="page page--5">
  <h2 class="section-title section-title--bold" style="top:36px;font-size:29px">Beer and Cider</h2>
  <div class="list" style="top:112px">
    <div class="entry"><div class="item">Liberty Organic Helles Lager Draft<span class="leader"></span><span class="cost">2.50 (½ pt) / 4.00 (pt)</span></div><span class="note">A reflection of the Munich Helles style. A pale balanced lager that uses a clean malt canvas to showcase traditional hops. (O, VG)</span></div>
    <div class="entry"><div class="item">Vaal Blonde Lager<svg><use href="#leaf"/></svg><svg><use href="#nofree"/></svg><span class="leader"></span><span class="cost">4.25 (33cl)</span></div><span class="note">33cl, Belgium (O, VG, GF) Gluten-free</span></div>
    <div class="entry"><div class="item">Wildmere Organic Cider<svg><use href="#leaf"/></svg><span class="leader"></span><span class="cost">5 (pt)</span></div><span class="note">RUSSETS (O, VG)</span></div>
    <div class="entry"><div class="item">Wayfarer Cider<span class="leader"></span><span class="cost">2.50 (½ pt) / 4.00 (pt)</span></div><span class="note">BRAMBLE HOG (VG), 4.5% abv medium cider, still. Savour the bittersweet richness of cider apples followed by dark notes of berries.</span></div>
    <div class="entry"><div class="item">Forager Cider (VG)<span class="leader"></span><span class="cost">4.95 (pt)</span></div><span class="note">BRAMBLE HOG (VG), 6% abv. Aromatic tannins and a balanced bittersweet finish. Gently sparkling</span></div>
    <div class="entry"><div class="item">Sweet Lark<span class="leader"></span><span class="cost">4.95 (pt)</span></div><span class="note">TOR ALES, 50 cl 4.2% abv</span></div>
    <div class="entry"><div class="item">Small Mighty Beer<span class="leader"></span><span class="cost">4.95 (pt)</span></div><span class="note">Low-alcohol locally brewed craft beer 2% abv (VG)</span></div>
    <div class="entry"><div class="item">Red Hawk<svg><use href="#leaf"/></svg><span class="leader"></span><span class="cost">3.75 (pt)</span></div><span class="note">NORTHERN ISLE BREWERY. Organic amber ale 4.5%, 33cl.</span></div>
    <div class="entry"><div class="item">Hops and Rye<span class="leader"></span><span class="cost">5.50 (pt)</span></div><span class="note">CUTTER &amp; KEEL 5.3% ABV 50CL. Unfiltered, unfined, unpasteurised and alive! Full-bodied and sweet with peppery rye malts and bright hops.</span></div>
  </div>
  <div class="legend"><span><svg><use href="#nofree"/></svg>Gluten free</span><span><svg><use href="#leaf"/></svg>Organic</span></div>
  <span class="page-number">05</span>
</section>

<!-- Page 06: Cocktails & Highballs -->
<section class="page page--6">
  <h2 class="section-title" style="top:24px;line-height:32px;font-size:30px">Cocktails &amp;<br>Highballs</h2>
  <div class="list" style="top:117px">
    <div class="entry"><div class="item">Monkey Nuts<svg><use href="#leaf"/></svg><svg><use href="#nut"/></svg><span class="leader"></span><span class="cost">7.50</span></div><span class="note">Organic amaretto liqueur with warm almond milk, honey and spices.</span></div>
    <div class="entry"><div class="item">Organic Bucks Fizz<span class="leader"></span><span class="cost">5.00</span></div><span class="note">Prosecco and orange juice.</span></div>
    <div class="entry"><div class="item">Bloody Mary<svg><use href="#celery"/></svg><span class="leader"></span><span class="cost">6.50</span></div><span class="note">Double vodka, tomato juice, Worcester sauce, pepper sauce, celery, seasoning.</span></div>
    <div class="entry"><div class="item">Pink G&amp;T<span class="leader"></span><span class="cost">6.50</span></div><span class="note">Double Heathland Gin and aromatic tonic, with a twist of lemon.</span></div>
    <div class="entry"><div class="item">Fairfield House G&amp;T<span class="leader"></span><span class="cost">6.50</span></div><span class="note">House gin with Indian tonic, garnished with a lemon wedge.</span></div>
    <div class="entry"><div class="item">Vodka &amp; Lemon<span class="leader"></span><span class="cost">6.50</span></div><span class="note">Orchard Vodka is a premium vodka made with heritage apples. Served with Sicilian Lemonade and fresh lemon.</span></div>
    <div class="entry"><div class="item">Vodka &amp; Tonic<span class="leader"></span><span class="cost">6.00</span></div><span class="note">Organic vodka with Indian tonic, garnished with a lemon twist.</span></div>
    <div class="entry"><div class="item">Cuba Libre<span class="leader"></span><span class="cost">6.00</span></div><span class="note">Caleta organic spiced rum with Kindred Cola.</span></div>
    <div class="entry"><div class="item">Whisky &amp; Ginger<svg><use href="#leaf"/></svg><span class="leader"></span><span class="cost">6.50</span></div><span class="note">Highland organic whisky with ginger beer, garnished with an orange twist.</span></div>
    <div class="entry"><div class="item">Rum &amp; Ginger<span class="leader"></span><span class="cost">6.00</span></div><span class="note">Caleta dark rum with ginger beer, garnished with lime wedges.</span></div>
    <div class="entry"><div class="item">Whisky Highball<svg><use href="#leaf"/></svg><span class="leader"></span><span class="cost">6.50</span></div><span class="note">Highland organic whisky with soda water, garnished with a lemon twist.</span></div>
    <div class="entry"><div class="item">Cognac &amp; Ginger<svg><use href="#leaf"/></svg><span class="leader"></span><span class="cost">6.00</span></div><span class="note">Maison Ardent organic cognac with ginger beer and slices of fresh ginger.</span></div>
    <div class="entry"><div class="item">Virgin Mary<svg><use href="#celery"/></svg><span class="leader"></span><span class="cost">2.95</span></div><span class="note">Tomato juice, Worcester sauce, pepper sauce, celery, seasoning.</span></div>
  </div>
  <div class="legend"><span><svg><use href="#nut"/></svg>Contain nuts</span><span><svg><use href="#celery"/></svg>With celery</span></div>
  <span class="page-number">06</span>
</section>
</body>
</html>
```